B2B Brochure design needed for "FRP Grating for Boardwalk Use" - about 12 pages - Not for print use

We need a design for a multipage brochure which will be used to promote one of our products, called DeckLume, which is FRP grating. We are specifically promoting its use for boardwalk decking with this brochure.
We require the brochure to be in US Letter size in pdf format that will be emailed to prospective clints and made available for download from our web site. This brochure will not be made into print
The brochure must look professional. We would prefer to use Helvetica Neue (light, regular, bold) font family for body text and Outfit (Light, regular, semibold) for the headings and the color scheme to use the colors as in doc. attached
Please use the copy and photos provided in the .zip file. (or extract them from the word doc). You can mix up the photos throughout the brochure where you best see fit. If you feel a photo isn't necessary or applicable, you can leave it out. I've added some extra photos if needed to fill out any section better (you could initially repeat photos on the pages and we can swap them out later). We may also decide to add extra text later, depending on the design proposed.
We want the title of the brochure to be “FRP Grating for Boardwalks".
With the cover page, one idea would be to use the outline of our current Velmorix logo for the main image and infill this with image(s) of applications (but don’t use the small image showing a section of grating that is in the Specifications section).
The cover page should display the DeckLume logo the at top, the brochure title ‘FRP Grating for Boardwalks’, our company name and logo at bottom and the web address www.velmorix.com close to it.
There are essentially four sections
Introduction
List of Benefits
Gallery pages showing examples of specific applications
Technical Data
The ‘Benefits’ section must show design consistency with all of the points mentioned.
Please do not think that adding multiple design elements or excess blocks of color will determine the design selected. Remember the phrase ‘Less is more’. I’ve attached an old Velmorix brochure for reference. Updating this brochure will most likely be posted as a later project.
You can refer to our website www.velmorix.com for further product information if needed You can also see the FRP for Boardwalks page on our website at: https://www.velmorix.com/fiberglass-grating-boardwalks/
I am attaching the following:
- Word doc containing copy and photos
- company logo
- company color schemes
- old Velmorix brochure for reference
Thanks for your consideration!

```html
<!DOCTYPE html>
<html lang="en">
<head>
<meta charset="utf-8">
<title>FRP Grating for Boardwalks Brochure</title>
<link href="https://fonts.googleapis.com/css2?family=Outfit:wght@300;400;600&family=Inter:wght@300;400;700&display=swap" rel="stylesheet">
<style>
:root{
  --board:#eceef2;
  --paper:#ffffff;
  --blue:#1f5c9a;
  --blue-dark:#17467a;
  --navy:#141c28;
  --ink:#2a2f36;
  --muted:#7b8591;
  --line:#d5dae0;
  --sky:#8fb3cf;
  --sea:#6e93a8;
  --wood:#8a5a3a;
  --green:#6f7d55;
  --grey:#9aa1a6;
}
*{margin:0;padding:0;box-sizing:border-box}
html,body{width:752px;height:1200px;overflow:hidden;background:var(--board)}
body{position:relative;font-family:"Inter",Helvetica,Arial,sans-serif;color:var(--ink)}
.board-title{position:absolute;top:20px;right:28px;font-size:8px;color:var(--muted);letter-spacing:.3px}
.page{position:absolute;background:var(--paper);overflow:hidden;box-shadow:0 1px 3px rgba(0,0,0,.08)}
.photo{position:absolute}
.abs{position:absolute}
.brand{font-family:"Outfit",sans-serif;font-weight:600;color:var(--blue);display:flex;align-items:center;gap:4px}
.brand .dot{width:7px;height:7px;background:var(--blue);border-radius:50%}
.brand.white{color:#fff}.brand.white .dot{background:#fff}
.brand.dark{color:var(--navy)}.brand.dark .dot{background:var(--navy)}
.h-band{font-family:"Outfit",sans-serif;font-weight:600;color:#fff;letter-spacing:.6px}
.body-text{font-size:4.2px;line-height:1.45;color:var(--ink)}
.body-text.light{color:#cfd6de}
.h-sub{font-family:"Outfit",sans-serif;font-weight:600;font-size:5px;color:var(--blue);margin:4px 0 1px}
.h-sub.light{color:#fff}
.tag{position:absolute;background:var(--blue);color:#fff;font-family:"Outfit",sans-serif;font-weight:600;font-size:6px;padding:3px 6px;letter-spacing:.4px;white-space:nowrap}
.spec-table{border-collapse:collapse;width:100%;font-size:3.6px;color:#fff}
.spec-table td{border-bottom:.5px solid rgba(255,255,255,.35);padding:1.3px 1px}
.data-table{border-collapse:collapse;width:100%;font-size:3.6px}
.data-table td{border-bottom:.5px solid var(--line);padding:1.3px 1px}
.data-table tr:first-child td{background:var(--blue);color:#fff;font-weight:700}
.fold{position:absolute;top:0;bottom:0;width:1px;background:rgba(0,0,0,.06)}
.sample{position:absolute;background:#fff;padding:5px}
.sample .photo{position:static;width:100%;height:100%}
</style>
</head>
<body>
<div class="board-title">FRP Grating For Boardwalks Brochure</div>

<section class="page cover" style="left:42px;top:75px;width:330px;height:262px">
  <div class="brand abs" style="left:20px;top:22px;font-size:12px"><span class="dot"></span>DeckLume</div>
  <div class="abs" style="left:0;top:54px;width:330px;height:26px;background:var(--blue)">
    <div class="h-band abs" style="left:20px;top:7px;font-size:11px">FRP GRATING FOR BOARDWALKS</div>
  </div>
  <div class="photo" role="img" aria-label="Coastal boardwalk with railing overlooking a bay and hills" style="left:0;top:80px;width:330px;height:150px;background:linear-gradient(180deg,#9cc0dc 0%,#c9dbe6 40%,#7a9a8c 62%,#8a5a3a 100%)"></div>
  <div class="abs" style="left:20px;top:240px;font-size:4.5px;color:var(--muted)">www.velmorix.com</div>
  <div class="brand dark abs" style="right:20px;top:236px;font-size:9px"><span class="dot"></span>Velmorix</div>
</section>

<section class="page spread" style="left:390px;top:75px;width:335px;height:262px">
  <div class="fold" style="left:167px"></div>
  <div class="photo" role="img" aria-label="Red-toned boardwalk curving along a grassy coast" style="left:0;top:0;width:167px;height:100px;background:linear-gradient(160deg,#a9c6dc,#7e9a7a 55%,#8b4b35)"></div>
  <div class="abs" style="left:0;top:100px;width:167px;height:36px;background:var(--blue)">
    <div class="brand white abs" style="left:10px;top:6px;font-size:7px"><span class="dot" style="width:5px;height:5px"></span>DeckLume</div>
    <div class="h-band abs" style="left:10px;top:20px;font-size:7px">FRP GRATING FOR BOARDWALKS</div>
  </div>
  <div class="abs body-text" style="left:10px;top:144px;width:147px">
    <p>DeckLume FRP grating gives boardwalks a strong, light and slip resistant surface that lasts for decades with very little care.</p>
    <p style="margin-top:3px">It will not rot, rust or splinter, and it lets light and water pass through to the ground below, protecting sensitive plants and habitats.</p>
    <p style="margin-top:3px">Panels are easy to cut and fit on site, keeping install time and cost low.</p>
  </div>
  <div class="abs body-text" style="left:177px;top:12px;width:70px">
    <div class="h-sub">Benefits of FRP Grating for Boardwalks</div>
    <div class="h-sub">Long Service Life</div><p>Resists rot, rust and insects in all climates.</p>
    <div class="h-sub">Slip Resistant</div><p>Gritted top gives safe footing when wet.</p>
    <div class="h-sub">Lightweight</div><p>Easy to carry and fit by hand.</p>
    <div class="h-sub">Low Upkeep</div><p>No painting, sealing or treatment needed.</p>
    <div class="h-sub">Eco Friendly</div><p>Lets light through to the plants below.</p>
  </div>
  <div class="photo" role="img" aria-label="Boardwalk with grey grating and railing" style="left:253px;top:12px;width:72px;height:52px;background:linear-gradient(160deg,#b8c8d4,#7d8a8e)"></div>
  <div class="photo" role="img" aria-label="Timber-framed walkway with dark grating" style="left:253px;top:70px;width:72px;height:52px;background:linear-gradient(160deg,#90a18a,#4d4e49)"></div>
  <div class="photo" role="img" aria-label="Brown grating walkway through grassland" style="left:253px;top:128px;width:72px;height:52px;background:linear-gradient(160deg,#a3b6c2,#7b5b44)"></div>
  <div class="photo" role="img" aria-label="Boardwalk through coastal scrub" style="left:253px;top:186px;width:72px;height:60px;background:linear-gradient(160deg,#8ea888,#8e5a3e)"></div>
</section>

<section class="page spread" style="left:42px;top:358px;width:330px;height:255px;background:var(--navy)">
  <div class="fold" style="left:165px;background:rgba(255,255,255,.08)"></div>
  <div class="photo" role="img" aria-label="Grey grating boardwalk through bushland" style="left:10px;top:12px;width:68px;height:86px;background:linear-gradient(160deg,#7f8f7a,#5a6068)"></div>
  <div class="abs body-text light" style="left:86px;top:14px;width:70px">
    <div class="h-sub light">Strength</div><p>High load rating for foot and light vehicle traffic.</p>
    <div class="h-sub light">Fire Safe</div><p>Low flame spread rating for bushfire zones.</p>
    <div class="h-sub light">Non Conductive</div><p>Safe near power lines and water.</p>
  </div>
  <div class="photo" role="img" aria-label="Walkway with timber posts and trees" style="left:10px;top:108px;width:146px;height:135px;background:linear-gradient(160deg,#6f8a5e,#7b6a55 60%,#9a9e9c)"></div>
  <div class="abs body-text light" style="left:175px;top:14px;width:68px">
    <div class="h-sub light">UV Stable</div><p>Colour holds strong under full sun.</p>
    <div class="h-sub light">Corrosion Proof</div><p>Ideal for salt water and wet sites.</p>
    <div class="h-sub light">Quick Install</div><p>Cut and fit with basic tools.</p>
  </div>
  <div class="photo" role="img" aria-label="Long straight boardwalk over wetland" style="left:250px;top:12px;width:70px;height:100px;background:linear-gradient(180deg,#b6c4cc,#7d8c7e 55%,#6a6d70)"></div>
  <div class="photo" role="img" aria-label="Grey grating path beside shrubs" style="left:175px;top:122px;width:145px;height:121px;background:linear-gradient(160deg,#8a9c88,#9ea3a6)"></div>
</section>

<section class="page spread" style="left:390px;top:358px;width:335px;height:255px">
  <div class="fold" style="left:167px"></div>
  <div class="photo" role="img" aria-label="Viewing platform over a coastal beach" style="left:8px;top:8px;width:152px;height:112px;background:linear-gradient(180deg,#a8c3d6,#bcc6c2 50%,#8b9a9e)"></div>
  <div class="tag" style="left:8px;top:108px">VIEWING PLATFORMS</div>
  <div class="photo" role="img" aria-label="Grating bridge walkway in a forest" style="left:175px;top:8px;width:152px;height:112px;background:linear-gradient(160deg,#6f8a60,#4d5a45 60%,#8a8f92)"></div>
  <div class="tag" style="left:175px;top:108px">BRIDGES &amp; BRIDGE WALKWAYS</div>
  <div class="photo" role="img" aria-label="Walkway running out across a lake" style="left:8px;top:135px;width:152px;height:112px;background:linear-gradient(180deg,#9eb8c8,#7c96a4 55%,#3e4248)"></div>
  <div class="tag" style="left:8px;top:135px">COASTAL &amp; LAKES</div>
  <div class="photo" role="img" aria-label="Grating stairway climbing a bushy slope" style="left:175px;top:135px;width:152px;height:112px;background:linear-gradient(160deg,#8a9a78,#7a7366 55%,#a2a5a6)"></div>
  <div class="tag" style="left:262px;top:135px">STAIRWAYS</div>
</section>

<section class="page spread" style="left:42px;top:638px;width:330px;height:262px">
  <div class="photo" role="img" aria-label="Access ramp with grey grating and rails" style="left:0;top:0;width:165px;height:130px;background:linear-gradient(160deg,#b9c7d1,#8c9792 55%,#a2a6a8)"></div>
  <div class="tag" style="left:8px;top:118px">ACCESS RAMPS</div>
  <div class="photo" role="img" aria-label="Red grating path through native bush" style="left:0;top:132px;width:165px;height:130px;background:linear-gradient(160deg,#6f7d55,#8a4a35 70%)"></div>
  <div class="tag" style="left:8px;top:132px">ENVIRONMENTALLY MATCHING COLORS</div>
  <div class="abs" style="left:165px;top:0;width:165px;height:262px;background:var(--blue)">
    <div class="h-band abs" style="left:10px;top:12px;font-size:11px">SPECIFICATIONS</div>
    <div class="abs" style="left:10px;top:32px;width:145px">
      <table class="spec-table">
        <tr><td>Panel size</td><td>1220 x 3660 mm</td></tr>
        <tr><td>Thickness</td><td>25 / 38 / 50 mm</td></tr>
        <tr><td>Open area</td><td>68%</td></tr>
        <tr><td>Weight</td><td>12.4 kg/m²</td></tr>
        <tr><td>Surface</td><td>Gritted</td></tr>
      </table>
    </div>
    <div class="sample" style="left:10px;top:86px;width:68px;height:48px">
      <div class="photo" role="img" aria-label="Sample of moulded square-mesh grating panel" style="background:linear-gradient(160deg,#8e959b,#5d646b)"></div>
    </div>
    <div class="sample" style="left:87px;top:86px;width:68px;height:48px">
      <div class="photo" role="img" aria-label="Sample of mini-mesh grating panel with gritted top" style="background:linear-gradient(160deg,#9aa1a6,#6b7278)"></div>
    </div>
    <div class="abs" style="left:10px;top:144px;width:145px">
      <table class="spec-table">
        <tr><td>Resin</td><td>Isophthalic polyester</td></tr>
        <tr><td>Fire rating</td><td>Class 1</td></tr>
        <tr><td>Load rating</td><td>5 kPa</td></tr>
        <tr><td>Colours</td><td>Grey, green, red, brown</td></tr>
        <tr><td>Warranty</td><td>25 years</td></tr>
        <tr><td>Standards</td><td>ASTM E84</td></tr>
      </table>
    </div>
    <div class="abs body-text light" style="left:10px;top:205px;width:145px">Full technical data sheets and load tables are available on request from our sales team.</div>
  </div>
</section>

<section class="page spread" style="left:390px;top:638px;width:335px;height:262px">
  <div class="fold" style="left:167px"></div>
  <div class="photo" role="img" aria-label="Adjustable support pedestal" style="left:12px;top:14px;width:44px;height:58px;background:linear-gradient(180deg,#3a3f45,#6b7178)"></div>
  <div class="abs" style="left:62px;top:16px;font-family:'Outfit',sans-serif;font-weight:600;font-size:7px;color:var(--blue)">STEPWISE PEDESTAL</div>
  <div class="abs body-text" style="left:62px;top:28px;width:95px">Adjustable pedestals set the grating level on uneven ground with no digging or concrete needed.</div>
  <div class="abs" style="left:12px;top:84px;width:145px">
    <table class="data-table">
      <tr><td>Model</td><td>Height range</td><td>Load</td></tr>
      <tr><td>SW-1</td><td>28 – 40 mm</td><td>800 kg</td></tr>
      <tr><td>SW-2</td><td>40 – 70 mm</td><td>800 kg</td></tr>
      <tr><td>SW-3</td><td>70 – 120 mm</td><td>750 kg</td></tr>
      <tr><td>SW-4</td><td>120 – 220 mm</td><td>700 kg</td></tr>
      <tr><td>SW-5</td><td>220 – 400 mm</td><td>600 kg</td></tr>
    </table>
  </div>
  <div class="abs body-text" style="left:12px;top:140px;width:145px">Each head locks the grating in place and a slope pad corrects falls up to 5%.</div>
  <div class="photo" role="img" aria-label="Tall pedestal support" style="left:185px;top:14px;width:40px;height:70px;background:linear-gradient(180deg,#3a3f45,#6b7178)"></div>
  <div class="abs body-text" style="left:232px;top:16px;width:92px">
    <div class="h-sub">Installation</div>
    <p>Place pedestals on a firm base, set the height, then lay the panels and fix with clips.</p>
    <div class="h-sub">Fixing Clips</div>
    <p>Stainless clips hold panels down against wind and foot traffic.</p>
  </div>
  <div class="abs" style="left:177px;top:196px;width:150px;display:flex;justify-content:space-between;align-items:flex-end">
    <div role="img" aria-label="Pedestal size one" style="width:18px;height:12px;background:#4a5058"></div>
    <div role="img" aria-label="Pedestal size two" style="width:18px;height:18px;background:#4a5058"></div>
    <div role="img" aria-label="Pedestal size three" style="width:18px;height:24px;background:#4a5058"></div>
    <div role="img" aria-label="Pedestal size four" style="width:18px;height:32px;background:#4a5058"></div>
    <div role="img" aria-label="Pedestal size five" style="width:18px;height:42px;background:#4a5058"></div>
  </div>
  <div class="abs" style="left:177px;top:242px;width:150px;display:flex;justify-content:space-between;font-size:3.6px;color:var(--muted)">
    <span>SW-1</span><span>SW-2</span><span>SW-3</span><span>SW-4</span><span>SW-5</span>
  </div>
</section>

<section class="page back-cover" style="left:42px;top:922px;width:330px;height:255px">
  <div class="brand dark abs" style="left:142px;top:190px;font-size:9px"><span class="dot"></span>Velmorix</div>
  <div class="abs" style="left:0;width:330px;top:206px;text-align:center;font-size:4.2px;color:var(--muted);line-height:1.5">
    www.velmorix.com &nbsp;|&nbsp; 1 800 555 0142 &nbsp;|&nbsp; info@velmorix.com<br>
    12 Harbour Lane, Portview, QLD 4000
  </div>
</section>
</body>
</html>
```